Is your Will up to date?

We need a flyer that invites people to ask themselves if their Will is up to date.
In addition it is a known fact that people do not adjust their Will as often as they should to reflect their current wishes and circumstances.
Also, a large number of people end up having their estate pay taxes
that could be avoided if correct planning is in place.
We are offering a free of charge service the carry out a check to make sure families have in place a Will that suits their needs and circumstances and that has taken into account the tax positions and impact fully with a view to having the estate as tax efficient as possible.
A Will service is also part of the family check up.

Below is the suggested text for the flyer

A Will is one of the most important documents that we should all have. Many people are aware that if they die without having made a Will, then intestate rules apply which means in simple terms, that family assets and cash could end up in the hands of the Treasury.

While many people have looked at and acted upon creating a Will, it is fair to say that for many, the terms and wishes of the Will are often outdated. It is easy to assume that amending a Will frequently is a complicated process which it need not be.

An individual or a family Will is most important in order to ensure that upon death, your estate is dealt with and distributed in accordance with your wishes. This is also to ensure that any family are looked after by those provisions. Not only may family changes and additions affect a family Will, but there are also life changing situations that can have an effect.

Additionally, consideration needs to be given regularly to the current tax position, with specific regard to Inheritance Tax and how estate values can be legitimately reduced resulting in less tax to pay.

At Hartwell & Company we have the advantage of our Chartered Accountancy practice background, as well as also being Independent Financial Advisers. We are therefore well placed to advise families on the creation or updating of their Will, and to give advice on how to minimise tax payments.

Even for individuals and families that have had no significant changes in circumstances for many years, very often the beneficiaries may need to be updated, and even the appointment of Executors and Trustees needs to be addressed because very often, these instructions are considerably out of date.

A Will and all of its complex implications should be reviewed every one or two years and it is an extremely simple process to do this with our assistance.

So far as minimising payments for tax there are a wide range of effective methods that help do this. As general examples, there can be gifts made to family or a partner, gifts to friends, charitable donations, the use of insurance products to help settle tax liability as well as looking at placing assets into Trust. We have a wealth of experience in setting up the different types of Trust that exist and can help you easily understand how they would work for you.

When looking at the preparation of a Will, there are hundreds of questions that could be considered appropriate. However, with our experience and knowledge, and bespoke software this process can be covered within an initial meeting of less than one hour. You will have the re-assurance of knowing that every aspect has been carefully considered in preparing a Will to your circumstances and wishes.

The initial meeting and any follow up meetings are completely free of all cost and charges, and can be held at either our offices, or at your home if preferred.

We can just as easily deal with the process over the telephone if more convenient. Thereafter, we will prepare a draft Will for you, and give you confirmation as to the charges. In most cases, an individual or family Will would not normally involve charges in excess of £100.

So far as mitigating possible Inheritance Tax liabilities on the estate, we also offer the benefit of an asset and investment review at no cost. The individual or family assets are carefully considered, along with your requirements of income and growth and any specific requests or wishes that you wish to build into any trust or other methods of your choosing.

At the initial meeting or conference call we discuss all of these implications and will prepare a report and recommendations for your consideration, again free of charge. If you decide to act upon any of the recommendations, then any fees can be discussed and agreed at that stage.

All in all, whether you require assistance in preparing or updating a Will, or receiving independent advice regarding your estate assets or investments, these functions are carried out by us at no initial costs or charges.

At every step of the way there are never hidden charges or fees that you will be asked to be paid. We have over 30 years of experience in these market places, and value the service we give our clients and the reputation we gain from it.

We consider the review of a Will should be carried out at a minimum of every two years and it is a very small financial budget to allow for, against having the satisfaction of knowing these important matters are reflecting your current views, circumstances and wishes.

The same can be said for any trust and investment matters and any estate advice given. We are extremely proud and confident of the service we provide, and if any of our clients decide they do not wish to act upon the advice given, then they at least have had the benefit of a thorough review together with a recommendation without obligations of any sort.

To discuss these matters further or to make arrangements for a meeting please call our offices or email to derek@hartwellco-mail.co.uk

Content will be uploaded with next 24 hours

I am updating the brief with the wording.
It needs to be spread over the front and back of the flyer in an easy to read non boring design

Our firm logo will be updated shorty plus our Institute logo
Please make the flyer as catchy and interesting as possible.
Its a relatively boring topic for most people so it has to be eye catching rather than reading a page in a book

We will increase the budget if we are presented with a design we really like

Please note slightly amended text uploaded today

Target Market(s)

middle to upper class residents

Industry/Entity Type

Investment

Requirements
Must have
• Web address
Easy to read and understand
To look and feel catchy and not like reading a book
Some catchy graphics about tax, money, families etc

Fields where I can easily insert text and other details

```html
<!DOCTYPE html>
<html lang="en">
<head>
<meta charset="utf-8">
<title>Hartwell &amp; Co. – Will review flyer</title>
<link rel="stylesheet" href="https://fonts.googleapis.com/css2?family=Fira+Sans:ital,wght@0,400;0,600;0,700;1,400;1,700&display=swap">
<style>
:root{
  --brand-red:#e31b2b;
  --ink:#1f1f1f;
  --muted-ink:#333;
  --pill:#4a4a4a;
  --paper:#ffffff;
  --backdrop:#e4e4e6;
  --photo-light:#eef1f4;
  --photo-mid:#d9c9b8;
}
*{box-sizing:border-box;margin:0;padding:0}
html,body{width:1200px;height:900px;overflow:hidden}
body{background:var(--backdrop);font-family:"Fira Sans",Arial,sans-serif;color:var(--ink);position:relative}
.page{position:absolute;top:88px;width:505px;height:652px;background:var(--paper);overflow:hidden;box-shadow:0 2px 8px rgba(0,0,0,.18)}
.page--front{left:87px}
.page--back{left:636px}
.page-art{position:absolute;inset:0;width:505px;height:652px}

.brand{position:absolute;left:24px;top:20px;background:var(--paper);padding:4px 8px 4px 4px;display:flex;align-items:flex-start;gap:8px}
.brand-square{width:34px;height:34px;background:var(--brand-red);flex:none}
.brand-name{font-weight:700;font-size:21px;color:var(--brand-red);line-height:1}
.brand-tagline{font-size:13px;color:var(--ink);margin-top:4px;font-style:italic}

.headline{position:absolute;left:0;right:0;top:400px;text-align:center;color:var(--brand-red);font-style:italic;font-weight:700;font-size:31px;line-height:42px;padding:0 30px}
.call-pill{position:absolute;right:27px;top:595px;background:var(--pill);color:#fff;border-radius:10px;padding:6px 10px;font-weight:600;font-size:14px;display:flex;align-items:baseline;gap:6px}
.call-pill small{font-weight:400;font-size:12px}

.body-columns{position:absolute;left:12px;right:10px;top:120px;height:478px;display:flex;gap:13px}
.body-column{flex:1;font-size:6.55px;line-height:1.36;color:var(--muted-ink);text-align:justify}
.body-column p{margin-bottom:7px}
.body-column .email{font-style:italic;font-weight:700;font-size:8px;color:var(--ink);margin-left:5px}

.contact-bar{position:absolute;left:44px;right:8px;top:624px;display:flex;align-items:center;gap:12px;color:var(--brand-red);font-size:10.5px}
.contact-item{display:flex;align-items:center;gap:4px;white-space:nowrap}
.contact-item--address{font-size:7px;font-weight:600;margin-left:auto}
.contact-item svg{flex:none}
</style>
</head>
<body>

<section class="page page--front">
  <svg class="page-art" viewBox="0 0 505 652" aria-hidden="true">
    <defs>
      <linearGradient id="photoTone" x1="0" y1="0" x2="1" y2="1">
        <stop offset="0" stop-color="var(--photo-light)"/>
        <stop offset=".55" stop-color="var(--photo-mid)"/>
        <stop offset="1" stop-color="#c9b29c"/>
      </linearGradient>
    </defs>
    <rect class="hero-photo" x="0" y="0" width="505" height="390" fill="url(#photoTone)"/>
    <path class="accent-arc" d="M410 0 Q360 170 505 330 L505 0 Z" fill="var(--brand-red)"/>
    <path class="accent-wave" d="M0 300 Q170 250 330 300 Q420 325 505 300 L505 395 Q260 320 0 400 Z" fill="var(--brand-red)"/>
    <path class="paper-sweep" d="M0 398 Q260 318 505 393 L505 652 L0 652 Z" fill="var(--paper)"/>
  </svg>
  <div role="img" aria-label="Photograph of an older couple reviewing their Will with a smiling adviser" style="position:absolute;left:0;top:60px;width:400px;height:230px"></div>

  <div class="brand">
    <span class="brand-square"></span>
    <div>
      <div class="brand-name">Hartwell &amp; Co.</div>
      <div class="brand-tagline">Chartered Accountants</div>
    </div>
  </div>

  <h1 class="headline">Advising families on the creation or updating of their Will, and how to minimise tax payments</h1>

  <div class="call-pill"><small>call</small>01632 960418</div>
</section>

<section class="page page--back">
  <svg class="page-art" viewBox="0 0 505 652" aria-hidden="true">
    <path class="corner-arc" d="M420 0 Q425 105 505 135 L505 0 Z" fill="var(--brand-red)"/>
    <circle cx="0" cy="652" r="42" fill="var(--brand-red)"/>
    <circle cx="0" cy="652" r="26" fill="var(--paper)"/>
    <circle cx="0" cy="652" r="12" fill="var(--brand-red)"/>
  </svg>

  <div class="brand">
    <span class="brand-square"></span>
    <div>
      <div class="brand-name">Hartwell &amp; Co.</div>
      <div class="brand-tagline">Chartered Accountants</div>
    </div>
  </div>

  <div class="body-columns">
    <div class="body-column">
      <p>A Will is one of the most important documents that we should all have. Many people are aware that if they die without having made a Will, then intestate rules apply which means in simple terms, that family assets and cash could end up in the hands of the Treasury.</p>
      <p>While many people have looked at and acted upon creating a Will, it is fair to say that for many, the terms and wishes of the Will are often outdated. It is easy to assume that amending a Will frequently is a complicated process which it need not be.</p>
      <p>An individual or a family Will is most important in order to ensure that upon death, your estate is dealt with and distributed in accordance with your wishes. This is also to ensure that any family are looked after by those provisions. Not only may family changes and additions affect a family Will, but there are also life changing situations that can have an effect.</p>
      <p>Additionally, consideration needs to be given regularly to the current tax position, with specific regard to Inheritance Tax and how estate values can be legitimately reduced resulting in less tax to pay.</p>
      <p>At Hartwell &amp; Company we have the advantage of our Chartered Accountancy practice background, as well as also being Independent Financial Advisers. We are therefore well placed to advise families on the creation or updating of their Will, and to give advice on how to minimise tax payments.</p>
      <p>Even for individuals and families that have had no significant changes in circumstances for many years, very often the beneficiaries may need to be updated, and even the appointment of Executors and Trustees needs to be addressed because very often, these instructions are considerably out of date.</p>
      <p>A Will and all of its complex implications should be reviewed every one or two years and it is an extremely simple process to do this with our assistance.</p>
      <p>So far as minimising payments for tax there are a wide range of effective methods that help do this. As general examples, there can be gifts made to family or a partner, gifts to friends, charitable donations, the use of insurance products to help settle tax liability as well as looking at placing assets into Trust. We have a wealth of experience in setting up the different types of Trust that exist and can help you easily understand how they would work for you.</p>
      <p>When looking at the preparation of a Will, there are hundreds of questions that could be considered appropriate. However, with our experience and knowledge, and bespoke software this process can be covered within an initial meeting of less than one hour. You will have the re-assurance of knowing that every aspect has been carefully considered in preparing a Will to your circumstances and wishes.</p>
    </div>
    <div class="body-column">
      <p>The initial meeting and any follow up meetings are completely free of all cost and charges, and can be held at either our offices, or at your home if preferred.</p>
      <p>We can just as easily deal with the process over the telephone if more convenient. Thereafter, we will prepare a draft Will for you, and give you confirmation as to the charges. In most cases, an individual or family Will would not normally involve charges in excess of £100.</p>
      <p>So far as mitigating possible Inheritance Tax liabilities on the estate, we also offer the benefit of an asset and investment review at no cost. The individual or family assets are carefully considered, along with your requirements of income and growth and any specific requests or wishes that you wish to build into any trust or other methods of your choosing.</p>
      <p>At the initial meeting or conference call we discuss all of these implications and will prepare a report and recommendations for your consideration, again free of charge. If you decide to act upon any of the recommendations, then any fees can be discussed and agreed at that stage.</p>
      <p>All in all, whether you require assistance in preparing or updating a Will, or receiving independent advice regarding your estate assets or investments, these functions are carried out by us at no initial costs or charges.</p>
      <p>At every step of the way there are never hidden charges or fees that you will be asked to be paid. We have over 30 years of experience in these market places, and value the service we give our clients and the reputation we gain from it.</p>
      <p>We consider the review of a Will should be carried out at a minimum of every two years and it is a very small financial budget to allow for, against having the satisfaction of knowing these important matters are reflecting your current views, circumstances and wishes.</p>
      <p>The same can be said for any trust and investment matters and any estate advice given. We are extremely proud and confident of the service we provide, and if any of our clients decide they do not wish to act upon the advice given, then they at least have had the benefit of a thorough review together with a recommendation without obligations of any sort.</p>
      <p>To discuss these matters further or to make arrangements for a meeting please call our offices or email to<br><span class="email">derek@hartwellco-mail.co.uk</span></p>
    </div>
  </div>

  <div class="contact-bar">
    <span class="contact-item">
      <svg width="11" height="11" viewBox="0 0 12 12" aria-hidden="true"><circle cx="6" cy="6" r="5.2" fill="none" stroke="currentColor" stroke-width="1.3"/><ellipse cx="6" cy="6" rx="2.2" ry="5.2" fill="none" stroke="currentColor" stroke-width="1"/><line x1="1" y1="6" x2="11" y2="6" stroke="currentColor" stroke-width="1"/></svg>
      www.hartwellandco.co.uk
    </span>
    <span class="contact-item">
      <svg width="10" height="11" viewBox="0 0 10 11" aria-hidden="true"><path d="M2 0.5 L4 2.8 L3 4.2 Q4 6.6 6.3 7.8 L7.6 6.8 L9.6 8.8 L8.2 10.4 Q4.5 10.2 1.8 6.6 Q0 4 0.4 1.6 Z" fill="currentColor"/></svg>
      01632 960418
    </span>
    <span class="contact-item contact-item--address">
      <svg width="9" height="9" viewBox="0 0 10 10" aria-hidden="true"><path d="M5 0.5 L9.6 4.6 L8.3 4.6 L8.3 9.5 L1.7 9.5 L1.7 4.6 L0.4 4.6 Z" fill="currentColor"/></svg>
      Mill House | Mill Lane | Westbury Green | Surrey | KT99 1AB
    </span>
  </div>
</section>

</body>
</html>
```